We need a tri-fold brochure for our business called: KindleSprout. (KindleSprout Therapy Services)
This is a therapy services business that offers Physiotherapy and Occupational Therapy to children aged 5 to 16 years of age. The focus is on Neuro-developmental therapy and the children have a range of conditions such as Cerebral-Palsy, brain injuries etc... We are looking for designs that focus on children, fun and the word nurture.
Target Market(s)
Primarily parents and people looking for therapy services.
Industry/Entity Type
Business
Font styles to use
Sans Serif

```html
<!DOCTYPE html>
<html lang="en">
<head>
<meta charset="utf-8">
<title>KindleSprout Therapy Services – Tri-fold Brochure</title>
<link rel="stylesheet" href="https://fonts.googleapis.com/css2?family=Exo+2:wght@600;700&family=Open+Sans:wght@600;700&display=swap">
<style>
  :root {
    --page-bg: #6d6d6f;
    --teal-deep: #0d665d;
    --teal: #18a090;
    --teal-light: #7fd6cb;
    --paper: #ffffff;
    --band-grey: #8d8d8f;
    --pill-grey-top: #a5aeb1;
    --pill-grey-bottom: #6f7b7e;
    --ink: #3a3a3c;
    --card-ink: #555;
  }
  * { box-sizing: border-box; margin: 0; padding: 0; }
  html, body { width: 1200px; height: 1000px; overflow: hidden; }
  body { background: var(--page-bg); font-family: "Open Sans", Arial, sans-serif; position: relative; }

  .brochure { position: absolute; left: 45px; top: 70px; width: 1110px; height: 860px; display: flex; box-shadow: 0 10px 30px rgba(0,0,0,.35); }
  .panel {
    position: relative; width: 370px; height: 860px; overflow: hidden;
    background: linear-gradient(180deg, var(--teal-deep) 0%, var(--teal) 20%, var(--teal-light) 42%, var(--paper) 56%, var(--paper) 100%);
  }
  .panel + .panel { border-left: 1px solid rgba(0,0,0,.08); }
  .panel-band { position: absolute; left: 0; bottom: 0; width: 100%; height: 70px; background: var(--band-grey); }

  .panel-title {
    position: absolute; left: 28px; top: 36px;
    font-family: "Exo 2", Arial, sans-serif; font-weight: 700; font-size: 34px;
    color: var(--paper); letter-spacing: 1px; text-transform: uppercase;
  }
  .body-copy { position: absolute; font-weight: 700; font-size: 13.5px; line-height: 1.35; }
  .body-copy.on-teal { color: var(--paper); }
  .body-copy.on-paper { color: var(--ink); }

  .photo { position: absolute; box-shadow: 0 4px 10px rgba(0,0,0,.25); }

  /* Who are we panel */
  .who-intro { left: 28px; top: 96px; width: 310px; }
  .who-photo { left: 20px; top: 160px; width: 172px; height: 250px; border-radius: 0 60px 0 0;
    background: linear-gradient(160deg, #d9b79a, #b98a6b 55%, #e6ddd3); }
  .who-column { left: 208px; top: 160px; width: 145px; }

  .tab-pill {
    position: absolute; left: 0; top: 432px; width: 175px; height: 52px;
    border-radius: 0 26px 26px 0;
    background: linear-gradient(180deg, var(--pill-grey-top), var(--pill-grey-bottom));
    font-family: "Exo 2", Arial, sans-serif; font-weight: 700; font-size: 26px; color: var(--paper);
    display: flex; align-items: center; padding-left: 26px; text-transform: uppercase;
  }
  .care-column { left: 24px; top: 505px; width: 150px; }
  .care-photo { right: 0; top: 440px; width: 170px; height: 270px; border-radius: 50px 0 0 50px;
    background: linear-gradient(150deg, #9cc45a, #7b69b8 55%, #e9e2ee); }

  /* Services panel */
  .services-list { position: absolute; left: 0; top: 120px; width: 100%; }
  .service { position: relative; height: 220px; }
  .service-photo { left: 22px; top: 0; width: 130px; height: 185px; border-radius: 16px; }
  .service:nth-child(1) .service-photo { background: linear-gradient(150deg, #6bb36a, #d88a4f); }
  .service:nth-child(2) .service-photo { background: linear-gradient(150deg, #5ea6d8, #3b6fae); }
  .service:nth-child(3) .service-photo { background: linear-gradient(150deg, #d9a65e, #b8603f); }
  .service-card {
    position: absolute; left: 118px; top: 22px; width: 232px; height: 150px;
    background: var(--paper); border-radius: 16px; box-shadow: 0 4px 12px rgba(0,0,0,.25);
    padding: 20px 18px 0 46px; color: var(--card-ink);
  }
  .service-name { font-family: "Exo 2", Arial, sans-serif; font-weight: 700; font-size: 14px; margin-bottom: 6px; color: var(--ink); }
  .service-text { font-size: 12px; font-weight: 600; line-height: 1.45; }

  /* Guidelines panel */
  .guide-copy { left: 28px; top: 96px; width: 318px; font-size: 14.5px; }
  .guide-photo { right: 18px; top: 258px; width: 222px; height: 245px; border-radius: 55px 0 0 0;
    background: linear-gradient(140deg, #e8762f 0%, #e8762f 35%, #6db6d9 60%, #3d3f45 100%); }
  .brand-pill {
    position: absolute; left: 22px; top: 340px; width: 84px; height: 370px; border-radius: 30px;
    background: linear-gradient(180deg, var(--pill-grey-top), var(--pill-grey-bottom));
    box-shadow: 0 4px 10px rgba(0,0,0,.2);
    display: flex; align-items: center; justify-content: center;
  }
  .brand-name {
    transform: rotate(-90deg); white-space: nowrap;
    font-family: "Exo 2", Arial, sans-serif; font-weight: 700; font-size: 34px; color: var(--paper);
  }
  .handprints { position: absolute; left: 150px; top: 545px; width: 200px; height: 150px; border-radius: 14px;
    background: linear-gradient(100deg, #9cd23e 0%, #f2d12a 30%, #e93f95 60%, #27aee6 100%); opacity: .9; }
</style>
</head>
<body>
  <main class="brochure">
    <section class="panel panel-about">
      <h2 class="panel-title">Who are we?</h2>
      <p class="body-copy on-teal who-intro">Lorem ipsum dolor sit amet. Lorem ipsum dolor sit amet. Lorem ipsum</p>
      <div class="photo who-photo" role="img" aria-label="Photo of a smiling mother hugging her young daughter"></div>
      <p class="body-copy on-teal who-column">Lorem ipsum dolor sit amet, consectetuer adipiscing elit, sed diam nonummy nibh euismod tincidunt ut laoreet dolore magna aliquam erat</p>
      <div class="tab-pill">We care</div>
      <p class="body-copy on-paper care-column">Lorem ipsum dolor sit amet, consectetuer adipiscing elit, sed diam nonummy nibh euismod tincidunt ut laoreet dolore magna aliquam erat volutpat. Ut wisi enim</p>
      <div class="photo care-photo" role="img" aria-label="Photo of a therapist playing with a young boy in a colourful therapy room"></div>
      <div class="panel-band"></div>
    </section>

    <section class="panel panel-services">
      <h2 class="panel-title">Our services</h2>
      <div class="services-list">
        <article class="service">
          <div class="photo service-photo" role="img" aria-label="Photo of a child during a physiotherapy session"></div>
          <div class="service-card">
            <h3 class="service-name">Physiotherapy Sessions</h3>
            <p class="service-text">Movement, strength and balance for growing bodies.</p>
          </div>
        </article>
        <article class="service">
          <div class="photo service-photo" role="img" aria-label="Photo of a child practising occupational therapy activities"></div>
          <div class="service-card">
            <h3 class="service-name">Occupational Therapy</h3>
            <p class="service-text">Building everyday skills for play and school.</p>
          </div>
        </article>
        <article class="service">
          <div class="photo service-photo" role="img" aria-label="Photo of a therapist guiding a child through play"></div>
          <div class="service-card">
            <h3 class="service-name">Neuro Development</h3>
            <p class="service-text">Gentle programs shaped around each child's needs.</p>
          </div>
        </article>
      </div>
      <div class="panel-band"></div>
    </section>

    <section class="panel panel-guidelines">
      <h2 class="panel-title">Our guidelines</h2>
      <p class="body-copy on-teal guide-copy">Lorem ipsum dolor sit amet, consectetuer adipiscing elit, sed diam nonummy nibh euismod tincidunt ut laoreet dolore Lorem ipsum dolor sit amet, consectetuer adipiscing elit, sed</p>
      <div class="photo guide-photo" role="img" aria-label="Photo of a laughing therapist with a happy boy in a wheelchair"></div>
      <div class="brand-pill"><span class="brand-name">KINDLESPROUT</span></div>
      <div class="handprints" role="img" aria-label="Colourful painted children's handprints in green, yellow, pink and blue"></div>
      <div class="panel-band"></div>
    </section>
  </main>
</body>
</html>
```